Marlow Brent Lawyers needs a web design

We need a web design for our conveyancing and commercial law firm based in Sydney Australia. We want to depersonalise the current website: http://www.marlowbrent-example.com/ and give it a classic modern feel to it. It should be a simple design (possibly one page) and communicate trust, professionalism and experience.

Content should include:

Marlow Brent is a boutique Sydney based legal practice specialising in business and property law.

We pride ourselves on our proactive, receptive and dynamic approach to client service. Our business survives on referrals from satisfied clients and professionals who respect the way we do business.

Practice areas

Business law

We act on the sale and purchase of businesses. We assist clients with structuring their businesses, drafting shareholder agreements and buy-sell arrangements. We have acted on a multitude of other commercial matters including franchising, distribution, marketing and business services (with a particular focus in the advertising sector).

Property law

We act for developers, commercial property investors, landlords and tenants. We also handle residential conveyancing and deal with strata and company title matters.

Private Client

We draft wills and codicils on behalf of clients and can also assist with applications for probate should the need arise.

Contact Us

Marlow Brent
Level 14, Arden Plaza
7 Wexcombe Lane
Sydney, NSW 2000

t: +61 (0)2 9471 6024
f: +61 (0)2 8352 7749
e: enquiries@marlowbrent-example.com

Target Market(s)

Individuals and business who need legal advice in the area of property and commercial law

Industry/Entity Type

Legal

Number of Pages Required

1 page

Font styles to use
Sans Serif

Requirements
Must have
• Clear and concise content.
Nice to have
• Some images to break up the content.
Should not have
• Any offensive images tones or connotations.

```html
<!DOCTYPE html>
<html lang="en">
<head>
<meta charset="utf-8">
<title>Marlow Brent Lawyers</title>
<link rel="stylesheet" href="https://fonts.googleapis.com/css2?family=Open+Sans:wght@400;600;700&family=Questrial&display=swap">
<style>
:root{
  --blue:#1346a0;
  --blue-dark:#0f3c8c;
  --ink:#222;
  --grey-text:#555;
  --light:#f3f3f3;
  --footer:#e4e4e4;
  --white:#fff;
  --black:#000;
}
*{margin:0;padding:0;box-sizing:border-box}
html,body{width:1200px;height:2230px;overflow:hidden}
body{font-family:"Open Sans",Arial,sans-serif;color:var(--ink);background:var(--white);position:relative}
.section{position:absolute;left:0;width:1200px}

/* top bar */
.topbar{top:0;height:54px;background:var(--blue);color:var(--white)}
.call{position:absolute;left:52px;top:9px;display:flex;align-items:center;gap:12px}
.call-icon{width:34px;height:34px;border-radius:50%;border:2px solid var(--white);display:flex;align-items:center;justify-content:center}
.call-label{font-size:11px;line-height:13px;opacity:.9}
.call-number{font-size:15px;font-weight:700;line-height:18px}
.social{position:absolute;right:38px;top:12px;display:flex;gap:12px}
.social span{width:26px;height:26px;border:1px solid rgba(255,255,255,.8)}

/* nav */
.navbar{top:54px;height:89px;background:var(--white)}
.brand{position:absolute;left:45px;top:18px}
.brand-name{font-size:31px;color:var(--blue);font-weight:400;line-height:34px}
.brand-sub{font-size:14px;color:var(--blue);text-align:right;line-height:18px}
.menu{position:absolute;left:605px;top:0;display:flex;height:89px;list-style:none}
.menu li{height:89px;display:flex;align-items:center;padding:0 33px;font-size:12px;color:#333}
.menu li.active{background:var(--blue);color:var(--white);padding:0 16px}

/* hero */
.hero{top:143px;height:609px;background:radial-gradient(ellipse at 25% 40%,#7a5a35 0%,#3c2a1b 40%,#241a14 75%,#1b1512 100%)}
.hero-title{position:absolute;top:195px;width:100%;text-align:center;font-family:"Questrial",sans-serif;color:var(--white);font-size:62px;line-height:74px;letter-spacing:1px}
.hero-btn{position:absolute;left:531px;top:395px;width:134px;height:55px;border:1px solid var(--white);border-radius:4px;color:var(--white);font-size:14px;display:flex;align-items:center;justify-content:center}
.hero-arrow{position:absolute;top:236px}

/* welcome */
.welcome{top:752px;height:292px;background:linear-gradient(#fff,#f1f1f1)}
.section-title{text-align:center;font-size:29px;font-weight:600;color:#333}
.section-title em{font-style:normal;color:var(--blue)}
.welcome .section-title{margin-top:46px}
.welcome-text{width:900px;margin:18px auto 0;text-align:center;font-size:11.5px;line-height:28px;color:var(--grey-text)}
.btn{display:flex;align-items:center;justify-content:center;background:var(--blue);color:var(--white);font-size:12px}
.welcome .btn{position:absolute;left:543px;top:210px;width:114px;height:33px}

/* practice */
.practice{top:1044px;height:574px;background:var(--white)}
.practice .section-title{margin-top:48px}
.link-line{position:absolute;left:300px;top:303px;width:640px;height:2px;background:var(--blue)}
.area{position:absolute;top:188px;width:240px;height:240px;transform:rotate(45deg);border-radius:26px;background:var(--black)}
.area.featured{background:var(--blue)}
.area-body{position:absolute;top:188px;width:240px;height:240px;display:flex;flex-direction:column;align-items:center;justify-content:center;color:var(--white);text-align:center}
.area-name{font-size:22px;font-weight:600}
.featured-body .area-name{font-size:17px}
.area-desc{font-size:11.5px;line-height:16px;width:210px;margin-top:10px}
.area-btn{margin-top:26px;background:var(--white);color:#333;font-size:11px;width:104px;height:34px;display:flex;align-items:center;justify-content:center;gap:6px}

/* testimonials */
.testimonials{top:1618px;height:276px;background:var(--light)}
.testimonials .section-title{margin-top:42px;font-size:28px;color:#111}
.portrait{position:absolute;left:208px;top:110px;width:118px;height:118px;border-radius:50%;border:5px solid var(--white);box-shadow:0 0 4px rgba(0,0,0,.25);background:radial-gradient(circle at 50% 40%,#f1dcc4,#c9b89f 60%,#9db8d8)}
.quote{position:absolute;left:372px;top:118px;width:670px;font-size:14.5px;line-height:25px;color:#444}
.author{position:absolute;right:163px;top:213px;font-size:19px;color:#111}
.t-arrow{position:absolute;top:148px}

/* footer */
.footer{top:1894px;height:261px;background:var(--footer)}
.col{position:absolute;top:40px}
.col h3{font-size:18px;font-weight:600;color:var(--blue);margin-bottom:22px}
.col p{font-size:11px;line-height:15px;color:#333}
.about{left:60px;width:265px}
.about .btn{width:108px;height:36px;margin-top:20px;gap:8px}
.news{left:410px;width:274px}
.news p{line-height:17px}
.email-field{margin-top:14px;height:37px;background:var(--white);border:1px solid #d6d6d6;font-size:10px;color:#aaa;padding:11px 12px}
.news .btn{height:36px;margin-top:10px;font-size:13px}
.cats{left:767px}
.cats ul{list-style:none}
.cats li{font-size:10.5px;line-height:22px;color:#333}
.cats li::before{content:"›";margin-right:10px;font-size:13px}
.contact{left:967px;width:200px}
.contact-row{display:flex;gap:10px;font-size:11px;line-height:17px;color:#333;margin-bottom:6px}
.contact-row svg{flex:none;margin-top:3px}

/* bottom */
.bottombar{top:2155px;height:75px;background:var(--blue);color:var(--white)}
.copyright{position:absolute;width:100%;top:30px;text-align:center;font-size:10px}
.bottom-social{position:absolute;right:48px;top:24px;display:flex;gap:10px}
.bottom-social span{width:28px;height:28px;border:1px solid var(--white)}
.bottom-social span.solid{background:var(--white)}
</style>
</head>
<body>

<header class="section topbar">
  <div class="call">
    <div class="call-icon">
      <svg width="16" height="16" viewBox="0 0 24 24"><path fill="#fff" d="M6.6 10.8a15 15 0 0 0 6.6 6.6l2.2-2.2a1 1 0 0 1 1-.25 11.4 11.4 0 0 0 3.6.57 1 1 0 0 1 1 1V20a1 1 0 0 1-1 1A17 17 0 0 1 3 4a1 1 0 0 1 1-1h3.5a1 1 0 0 1 1 1c0 1.25.2 2.45.57 3.57a1 1 0 0 1-.25 1z"/></svg>
    </div>
    <div>
      <div class="call-label">CALL US</div>
      <div class="call-number">1800 555 0142</div>
    </div>
  </div>
  <div class="social"><span></span><span></span><span></span></div>
</header>

<nav class="section navbar">
  <div class="brand">
    <div class="brand-name">Marlow Brent</div>
    <div class="brand-sub">Lawyers</div>
  </div>
  <ul class="menu">
    <li class="active">HOME</li>
    <li>OUR PEOPLE</li>
    <li>PRACTICE AREAS</li>
    <li>TESTIMONIALS</li>
    <li>CONTACT US</li>
  </ul>
</nav>

<section class="section hero" role="img" aria-label="Photo of a bronze statue of Lady Justice holding scales in front of law books">
  <svg class="hero-arrow" style="left:46px" width="36" height="36" viewBox="0 0 36 36"><circle cx="18" cy="18" r="16.5" fill="none" stroke="#fff" stroke-width="1.5"/><path d="M21 11l-7 7 7 7" fill="none" stroke="#fff" stroke-width="2.5"/></svg>
  <svg class="hero-arrow" style="left:1115px" width="36" height="36" viewBox="0 0 36 36"><circle cx="18" cy="18" r="16.5" fill="none" stroke="#fff" stroke-width="1.5"/><path d="M15 11l7 7-7 7" fill="none" stroke="#fff" stroke-width="2.5"/></svg>
  <h1 class="hero-title">WE'LL HELP YOU HANDLE<br>YOUR LEGAL CHALLENGE</h1>
  <div class="hero-btn">CLICK HERE</div>
</section>

<section class="section welcome">
  <h2 class="section-title">Welcome to <em>Marlow Brent Lawyer</em></h2>
  <p class="welcome-text">Lorem ipsum dolor sit amet, consectetur adipiscing elit, sed do eiusmod tempor incididunt ut labore et dolore magna aliqua. Ut enim ad minim veniam, quis nostrud exercitation ullamco laboris nisi ut aliquipLorem ipsum dolor sit amet, consectetur adipiscing elit, sed do eiusmod tempor incididunt ut labore et dolore magna aliqua. Ut enim ad minim veniam, quis nostrud exercitation ullamco laboris nisi ut aliquip</p>
  <div class="btn">READ MORE</div>
</section>

<section class="section practice">
  <h2 class="section-title">Practice <em>Areas</em></h2>
  <div class="link-line"></div>

  <div class="area featured" style="left:145px"></div>
  <div class="area-body featured-body" style="left:145px">
    <div class="area-name">Business law</div>
    <div class="area-desc">We act on the sale and purchase of businesses. We assist clients with structuring their businesses</div>
    <div class="area-btn">READ MORE <svg width="6" height="8" viewBox="0 0 6 8"><path d="M0 0l6 4-6 4z" fill="#333"/></svg></div>
  </div>

  <div class="area" style="left:487px"></div>
  <div class="area-body" style="left:487px">
    <div class="area-name">Property law</div>
    <div class="area-btn">READ MORE</div>
  </div>

  <div class="area" style="left:827px"></div>
  <div class="area-body" style="left:827px">
    <div class="area-name">Private Client</div>
    <div class="area-btn">READ MORE</div>
  </div>
</section>

<section class="section testimonials">
  <h2 class="section-title">Our <em>Testimonials</em></h2>
  <svg class="t-arrow" style="left:58px" width="18" height="26" viewBox="0 0 18 26"><path d="M14 3L5 13l9 10" fill="none" stroke="#1346a0" stroke-width="4"/></svg>
  <svg class="t-arrow" style="left:1122px" width="18" height="26" viewBox="0 0 18 26"><path d="M4 3l9 10-9 10" fill="none" stroke="#1346a0" stroke-width="4"/></svg>
  <div class="portrait" role="img" aria-label="Photo of a smiling senior couple"></div>
  <p class="quote">Lorem ipsum dolor sit amet, ctetuer adipiscing elit. Praesent vestibulum molestie lacus. Aenean nonummy hendrerit mauris. Phasellus porta. Fusce suscipit varius mi. Cum sociis natoque penatibus et magnis dis parturient.Lorem ipsum dolor sit amet</p>
  <div class="author">-Dana Whitford</div>
</section>

<footer class="section footer">
  <div class="col about">
    <h3>About us</h3>
    <p>Lorem ipsum dolor sit amet, consectetur adipiscing elit, sed do eiusmod tempor incididunt ut labore et dolore magna aliqua. Ut enim ad minim veniam, quis nostrud exercitation ullamco laboris nisi ut aliqui</p>
    <div class="btn">Read More <svg width="6" height="9" viewBox="0 0 6 9"><path d="M0 0l6 4.5L0 9z" fill="#fff"/></svg></div>
  </div>
  <div class="col news">
    <h3>Newsletter Signup</h3>
    <p>Subscribe our newsletter to know our daily updates and offer daily updates</p>
    <div class="email-field">Enter your Email Id</div>
    <div class="btn">SUBSCRIBE</div>
  </div>
  <div class="col cats">
    <h3>Categories</h3>
    <ul>
      <li>Home</li>
      <li>Our People</li>
      <li>Practice Areas</li>
      <li>Testimonials</li>
      <li>Contact Us</li>
    </ul>
  </div>
  <div class="col contact">
    <h3>Contact us</h3>
    <div class="contact-row">
      <svg width="9" height="12" viewBox="0 0 9 12"><path d="M4.5 0A4.5 4.5 0 0 0 0 4.5C0 8 4.5 12 4.5 12S9 8 9 4.5A4.5 4.5 0 0 0 4.5 0zm0 6.3a1.8 1.8 0 1 1 0-3.6 1.8 1.8 0 0 1 0 3.6z" fill="#1346a0"/></svg>
      <div>Marlow Brent<br>Level 14, Arden Plaza<br>7 Wexcombe Lane<br>Sydney, NSW 2000</div>
    </div>
    <div class="contact-row">
      <svg width="10" height="10" viewBox="0 0 24 24"><path fill="#1346a0" d="M6.6 10.8a15 15 0 0 0 6.6 6.6l2.2-2.2a1 1 0 0 1 1-.25 11.4 11.4 0 0 0 3.6.57 1 1 0 0 1 1 1V20a1 1 0 0 1-1 1A17 17 0 0 1 3 4a1 1 0 0 1 1-1h3.5a1 1 0 0 1 1 1c0 1.25.2 2.45.57 3.57a1 1 0 0 1-.25 1z"/></svg>
      <div>Office: +61 (0)2 9471 6024</div>
    </div>
    <div class="contact-row">
      <svg width="10" height="10" viewBox="0 0 10 10"><rect x="2" y="0" width="6" height="3" fill="#1346a0"/><rect x="0" y="3.5" width="10" height="6.5" rx="1" fill="#1346a0"/></svg>
      <div>Office: +61 (0)2 8352 7749</div>
    </div>
    <div class="contact-row">
      <svg width="10" height="8" viewBox="0 0 10 8"><rect width="10" height="8" fill="#1346a0"/><path d="M0 0l5 4 5-4" fill="none" stroke="#fff" stroke-width="1"/></svg>
      <div>info@marlowbrent-example.com</div>
    </div>
  </div>
</footer>

<div class="section bottombar">
  <div class="copyright">Copyright 2015 Marlow Brent All Rights Reserved.</div>
  <div class="bottom-social"><span></span><span></span><span class="solid"></span><span></span></div>
</div>

</body>
</html>
```